Surgery Office Letterhead Design

I'm seeking new letterhead that will comprise all of our office locations and logo and other applicable information, per the following:

Office Locations:

Lakemont Institute for Jaw & Face Surgery at Cleburne
347 Hazelpine Court
Harlow Springs, Texas 75917
Phone 817.382.4706
Fax 817.382.9034

Lakemont Institute for Jaw & Face Surgery at Stephenville
518 Willowgate Boulevard
Brennan Falls, Texas 75628
Phone 254.563.2781
Fax 254.563.2789

Lakemont Institute for Jaw & Face Surgery at Belton
739 West 9th Avenue
Marlow Ridge, Texas 75384
Phone 254.871.4035
Fax 254.871.4042

Other Info to include:

www.lakemontjawface.com
hello@lakemontjawface.com

Industry/Entity Type

Medical

Font styles to use
Serif
Sans Serif

Requirements
Must have
• See Project Description

```html
<!DOCTYPE html>
<html lang="en">
<head>
<meta charset="utf-8">
<title>Lakemont Institute for Jaw &amp; Face Surgery — Letterhead</title>
<link rel="stylesheet" href="https://fonts.googleapis.com/css2?family=Cinzel:wght@500&family=Open+Sans:wght@400&display=swap">
<style>
  :root {
    --backdrop: #e4e5e8;
    --paper: #ffffff;
    --navy: #1f2d5a;
    --ink: #2b2e36;
    --rule: #c9ccd3;
    --watermark: #eceef3;
  }
  html, body {
    margin: 0;
    width: 1200px;
    height: 936px;
    overflow: hidden;
    background: var(--backdrop);
  }
  .letterhead {
    position: absolute;
    left: 290px;
    top: 30px;
    width: 620px;
    height: 876px;
    background: var(--paper);
    box-shadow: 0 2px 10px rgba(0,0,0,.12);
    font-family: "Open Sans", Arial, sans-serif;
    color: var(--ink);
  }
  .brand {
    position: absolute;
    left: 38px;
    top: 42px;
    display: flex;
    align-items: center;
    gap: 10px;
    color: var(--navy);
    font-family: "Cinzel", Georgia, serif;
    font-weight: 500;
  }
  .brand-dot {
    width: 30px; height: 30px;
    border-radius: 50%;
    background: var(--navy);
  }
  .brand-name { font-size: 19px; line-height: 1.05; letter-spacing: .3px; }
  .brand-sub { font-size: 10.5px; letter-spacing: .6px; }
  .web-contact {
    position: absolute;
    right: 40px;
    top: 42px;
    padding-left: 12px;
    border-left: 1px solid var(--rule);
    font-size: 9.5px;
    line-height: 16px;
  }
  .web-contact div, .office-line { display: flex; align-items: center; gap: 5px; }
  .icon { width: 10px; height: 10px; flex: none; }
  .watermark {
    position: absolute;
    left: 200px;
    top: 300px;
    width: 220px;
    height: 220px;
    border-radius: 50%;
    background: var(--watermark);
  }
  .offices {
    position: absolute;
    right: 40px;
    bottom: 46px;
    width: 420px;
    font-size: 9.5px;
  }
  .office-line {
    padding: 6px 0;
    border-bottom: 1px solid var(--rule);
    white-space: nowrap;
  }
  .office-line:last-child { border-bottom: none; }
  .office-line .num { margin-right: 8px; }
</style>
</head>
<body>
<svg width="0" height="0" style="position:absolute">
  <defs>
    <symbol id="i-pin" viewBox="0 0 10 10"><circle cx="5" cy="5" r="5" fill="#1f2d5a"/><path d="M5 2.2a1.8 1.8 0 0 0-1.8 1.8C3.2 5.4 5 7.8 5 7.8S6.8 5.4 6.8 4A1.8 1.8 0 0 0 5 2.2z" fill="#fff"/></symbol>
    <symbol id="i-phone" viewBox="0 0 10 10"><circle cx="5" cy="5" r="4.4" fill="none" stroke="#1f2d5a" stroke-width="1"/><path d="M3.4 3c.3-.3.7-.2.8.1l.4.8-.5.5c.3.6.7 1 1.3 1.3l.5-.5.8.4c.3.1.4.5.1.8-.5.5-1.6.2-2.5-.7S2.9 3.5 3.4 3z" fill="#1f2d5a"/></symbol>
    <symbol id="i-fax" viewBox="0 0 10 10"><rect x="1" y="4" width="8" height="4.5" rx="1" fill="#1f2d5a"/><rect x="2.8" y="1.5" width="4.4" height="3" fill="#1f2d5a"/><rect x="3.3" y="6" width="3.4" height="1" fill="#fff"/></symbol>
    <symbol id="i-mail" viewBox="0 0 10 10"><circle cx="5" cy="5" r="5" fill="#1f2d5a"/><rect x="2.5" y="3.3" width="5" height="3.4" fill="#fff"/><path d="M2.5 3.3 5 5.3 7.5 3.3" fill="none" stroke="#1f2d5a" stroke-width=".7"/></symbol>
    <symbol id="i-web" viewBox="0 0 10 10"><circle cx="5" cy="5" r="5" fill="#1f2d5a"/><circle cx="5" cy="5" r="2.8" fill="none" stroke="#fff" stroke-width=".7"/><path d="M2.2 5h5.6M5 2.2c-1.4 1.6-1.4 4 0 5.6M5 2.2c1.4 1.6 1.4 4 0 5.6" fill="none" stroke="#fff" stroke-width=".6"/></symbol>
  </defs>
</svg>

<main class="letterhead">
  <header class="brand">
    <span class="brand-dot"></span>
    <div>
      <div class="brand-name">Lakemont Institute</div>
      <div class="brand-sub">For Jaw &amp; Face Surgery</div>
    </div>
  </header>

  <div class="web-contact">
    <div><svg class="icon"><use href="#i-mail"/></svg>hello@lakemontjawface.com</div>
    <div><svg class="icon"><use href="#i-web"/></svg>www.lakemontjawface.com</div>
  </div>

  <div class="watermark" role="img" aria-label="Faint brand emblem watermark"></div>

  <footer class="offices">
    <div class="office-line">
      <svg class="icon"><use href="#i-pin"/></svg><span class="num">347 Hazelpine Court, Harlow Springs, Texas 75917</span>
      <svg class="icon"><use href="#i-phone"/></svg><span class="num">817.382.4706</span>
      <svg class="icon"><use href="#i-fax"/></svg><span>817.382.9034</span>
    </div>
    <div class="office-line">
      <svg class="icon"><use href="#i-pin"/></svg><span class="num">518 Willowgate Boulevard, Brennan Falls, Texas 75628</span>
      <svg class="icon"><use href="#i-phone"/></svg><span class="num">254.563.2781</span>
      <svg class="icon"><use href="#i-fax"/></svg><span>254.563.2789</span>
    </div>
    <div class="office-line">
      <svg class="icon"><use href="#i-pin"/></svg><span class="num">739 West 9th Avenue, Marlow Ridge, Texas 75384</span>
      <svg class="icon"><use href="#i-phone"/></svg><span class="num">254.871.4035</span>
      <svg class="icon"><use href="#i-fax"/></svg><span>254.871.4042</span>
    </div>
  </footer>
</main>
</body>
</html>
```